Business Card for a Wedding Films Business

We require a business card design for our business 'Lewis Marrow Wedding Films'. The logo needs to look classy and high end.

Target Market(s)

Wedding Couples

Contact Information for Business Card

Lewis Marrow Wedding Films
07312 605 227
films@lewismarrowreels.com
www.lewismarrowreels.com

Facebook: @lewismarrowweddingfilms
Instagram: @lewismarrowfilms

Font styles to use
Sans Serif

Requirements
Must have
• Social media icons - Facebook and Instagram

```html
<!DOCTYPE html>
<html lang="en">
<head>
<meta charset="utf-8">
<title>Lewis Marrow Wedding Films – Business Card</title>
<link href="https://fonts.googleapis.com/css2?family=Jost:wght@400;500&family=Josefin+Sans:wght@300;400&display=swap" rel="stylesheet">
<style>
  :root {
    --backdrop: #161616;
    --card-white: #f7f7f7;
    --card-black: #0d0d0d;
    --ink: #111111;
    --ink-soft: #8a8a8a;
    --rule: #9a9a9a;
    --silver: #e6e6e6;
  }
  * { margin: 0; padding: 0; box-sizing: border-box; }
  html, body { width: 1200px; height: 900px; overflow: hidden; }
  body {
    background: var(--backdrop);
    display: flex;
    flex-direction: column;
    align-items: center;
    justify-content: center;
    gap: 40px;
  }
  .card {
    width: 630px;
    height: 360px;
    position: relative;
    box-shadow: 0 12px 30px rgba(0,0,0,.6);
  }
  .card--front { background: var(--card-white); color: var(--ink); }
  .card--back {
    background: var(--card-black);
    display: flex;
    align-items: center;
    justify-content: center;
  }
  .brand {
    font-family: 'Jost', sans-serif;
    font-weight: 500;
    text-transform: uppercase;
    line-height: 1.15;
    text-align: center;
  }
  .brand__name { display: block; font-size: 24px; letter-spacing: .22em; }
  .brand__tag { display: block; font-size: 12px; letter-spacing: .42em; }
  .card--front .brand { position: absolute; left: 36px; top: 30px; color: var(--ink); }
  .card--back .brand { color: var(--silver); }
  .card--back .brand__name { font-size: 30px; }
  .card--back .brand__tag { font-size: 15px; }
  .person {
    position: absolute;
    left: 36px;
    top: 112px;
    right: 0;
  }
  .person__name {
    font-family: 'Jost', sans-serif;
    font-weight: 400;
    font-size: 24px;
    letter-spacing: .02em;
    text-transform: uppercase;
  }
  .person__role {
    display: flex;
    align-items: center;
    gap: 4px;
    font-family: 'Josefin Sans', sans-serif;
    font-weight: 300;
    font-size: 14px;
    color: var(--ink-soft);
    margin-top: 2px;
  }
  .person__role::after {
    content: "";
    flex: 1;
    height: 1px;
    background: var(--rule);
    margin-right: 18px;
  }
  .contact-list, .social-list {
    list-style: none;
    position: absolute;
    font-family: 'Josefin Sans', sans-serif;
    font-weight: 300;
    font-size: 15px;
    color: var(--ink-soft);
  }
  .contact-list { left: 36px; top: 176px; }
  .social-list { right: 40px; bottom: 34px; }
  .contact-list li, .social-list li {
    display: flex;
    align-items: center;
    gap: 8px;
    height: 23px;
  }
  .icon { width: 14px; height: 14px; flex: none; }
  .icon circle.bg { fill: var(--ink); }
  .icon .glyph { fill: none; stroke: #fff; stroke-width: 1.3; }
  .network-marker {
    width: 14px;
    height: 14px;
    border-radius: 50%;
    background: var(--ink);
    flex: none;
  }
</style>
</head>
<body>
  <section class="card card--front" aria-label="Card front">
    <div class="brand">
      <span class="brand__name">Lewis Marrow</span>
      <span class="brand__tag">Wedding Films</span>
    </div>

    <div class="person">
      <h1 class="person__name">Lewis Marrow</h1>
      <p class="person__role">Photographer</p>
    </div>

    <ul class="contact-list">
      <li>
        <svg class="icon" viewBox="0 0 14 14" aria-hidden="true"><circle class="bg" cx="7" cy="7" r="7"/><path class="glyph" d="M4.3 4.2c0 3 2.5 5.6 5.5 5.6l.6-1.5-1.5-.7-.7.8c-1-.5-1.8-1.3-2.3-2.3l.8-.7-.7-1.5z"/></svg>
        07312 605 227
      </li>
      <li>
        <svg class="icon" viewBox="0 0 14 14" aria-hidden="true"><circle class="bg" cx="7" cy="7" r="7"/><rect class="glyph" x="3.6" y="4.6" width="6.8" height="4.8"/><path class="glyph" d="M3.6 4.6 7 7.3l3.4-2.7"/></svg>
        films@lewismarrowreels.com
      </li>
      <li>
        <svg class="icon" viewBox="0 0 14 14" aria-hidden="true"><circle class="bg" cx="7" cy="7" r="7"/><circle class="glyph" cx="7" cy="7" r="3.4"/><path class="glyph" d="M3.6 7h6.8M7 3.6c-1.6 2-1.6 4.8 0 6.8M7 3.6c1.6 2 1.6 4.8 0 6.8"/></svg>
        www.lewismarrowreels.com
      </li>
    </ul>

    <ul class="social-list" aria-label="Social media">
      <li><span class="network-marker" role="img" aria-label="Social network page"></span>@lewismarrowweddingfilms</li>
      <li><span class="network-marker" role="img" aria-label="Photo sharing profile"></span>@lewismarrowfilms</li>
    </ul>
  </section>

  <section class="card card--back" aria-label="Card back">
    <div class="brand">
      <span class="brand__name">Lewis Marrow</span>
      <span class="brand__tag">Wedding Films</span>
    </div>
  </section>
</body>
</html>
```